PowerPoint design MervoSan

We need a PowerPoint set-up based upon our existing logo (see joint file)
Our company is operating in the health care and life science sector. We are mainly focussing on international business

Target Market(s)

International

Industry/Entity Type

health care and life sciences

Requirements
Must have
• Logos as added

```html
<!DOCTYPE html>
<html lang="en">
<head>
<meta charset="utf-8">
<title>MervoSan – Table Sample Slide</title>
<link href="https://fonts.googleapis.com/css2?family=Carlito:ital,wght@0,400;0,700;1,400&display=swap" rel="stylesheet">
<style>
  :root {
    --navy: #0b4a80;
    --green: #5cbf1e;
    --ink: #3a3a3a;
    --rule: #cfd4da;
    --highlight: #d9d9d9;
    --paper: #ffffff;
  }
  * { box-sizing: border-box; margin: 0; padding: 0; }
  html, body { width: 1200px; height: 675px; overflow: hidden; background: var(--paper); }
  body { font-family: "Carlito", "Calibri", Arial, sans-serif; color: var(--ink); }
  .slide { position: relative; width: 1200px; height: 675px; }

  .accent { position: absolute; }
  .accent--left { left: 0; top: 64px; }
  .accent--right { left: 1146px; top: 100px; }

  .slide-title { position: absolute; left: 72px; top: 54px; font-size: 34px; font-weight: 700; color: var(--navy); letter-spacing: -0.2px; }
  .tagline { position: absolute; left: 72px; top: 114px; font-size: 20px; font-style: italic; color: var(--green); }

  .brand { position: absolute; left: 958px; top: 54px; display: flex; align-items: center; gap: 10px; }
  .brand__dot { width: 40px; height: 40px; border-radius: 50%; background: var(--navy); }
  .brand__name { font-size: 26px; font-weight: 700; color: var(--navy); }

  .col-head { position: absolute; top: 178px; height: 39px; width: 128px; background: var(--navy); color: #fff; font-weight: 700; font-size: 14px; display: flex; align-items: center; justify-content: center; }

  .row { position: absolute; left: 72px; width: 1057px; height: 50px; border: 1px solid var(--rule); }
  .row__head { position: absolute; left: 8px; top: 0; height: 100%; display: flex; align-items: center; font-size: 14px; font-weight: 700; color: var(--navy); }
  .cell { position: absolute; top: 12px; width: 106px; height: 25px; margin-left: -53px; display: flex; align-items: center; justify-content: center; font-size: 14px; }
  .cell--key { background: var(--highlight); font-weight: 700; }
  .c1 { left: 401px; } .c2 { left: 548px; } .c3 { left: 696px; } .c4 { left: 844px; } .c5 { left: 992px; }

  .footer-line { position: absolute; top: 614px; height: 1px; }
  .footer-line--left { left: 0; width: 708px; background: var(--navy); }
  .footer-line--right { left: 1146px; width: 54px; background: var(--green); }
  .footer-dot { position: absolute; top: 611px; width: 7px; height: 7px; border-radius: 50%; }
  .footer-dot--navy { left: 705px; background: var(--navy); }
  .footer-dot--green { left: 1143px; background: var(--green); }
  .deck-title { position: absolute; left: 725px; top: 608px; font-size: 10px; font-variant: small-caps; letter-spacing: 0.3px; color: var(--ink); }
  .page-number { position: absolute; left: 1112px; top: 607px; font-size: 11px; color: var(--ink); }
  .notes { position: absolute; left: 72px; top: 619px; font-size: 7.5px; line-height: 10.5px; color: var(--ink); list-style: none; }
</style>
</head>
<body>
<main class="slide">
  <svg class="accent accent--left" width="64" height="24" viewBox="0 0 64 24" aria-hidden="true">
    <rect x="0" y="9" width="64" height="3" fill="#0b4a80"/>
    <rect x="0" y="14" width="64" height="3" fill="#5cbf1e"/>
  </svg>
  <h1 class="slide-title">Slide Title – Table Sample</h1>
  <p class="tagline">Sample Tagline Text</p>

  <div class="brand">
    <span class="brand__dot"></span>
    <span class="brand__name">MervoSan</span>
  </div>
  <svg class="accent accent--right" width="54" height="24" viewBox="0 0 54 24" aria-hidden="true">
    <rect x="0" y="9" width="54" height="3" fill="#5cbf1e"/>
    <rect x="0" y="14" width="54" height="3" fill="#0b4a80"/>
  </svg>

  <div class="col-head" style="left:409px">Heading</div>
  <div class="col-head" style="left:557px">Heading</div>
  <div class="col-head" style="left:704px">Heading</div>
  <div class="col-head" style="left:852px">Heading</div>
  <div class="col-head" style="left:1000px">Heading</div>

  <div class="row" style="top:230px"><span class="row__head">Sample Row Heading</span>
    <span class="cell c1 cell--key">Content</span><span class="cell c2">Content</span><span class="cell c3">Content</span><span class="cell c4">Content</span><span class="cell c5">Content</span></div>
  <div class="row" style="top:293px"><span class="row__head">Sample Row Heading</span>
    <span class="cell c1">Content</span><span class="cell c2">Content</span><span class="cell c3">Content</span><span class="cell c4">Content</span><span class="cell c5 cell--key">Content</span></div>
  <div class="row" style="top:355px"><span class="row__head">Sample Row Heading</span>
    <span class="cell c1">Content</span><span class="cell c2">Content</span><span class="cell c3 cell--key">Content</span><span class="cell c4">Content</span><span class="cell c5">Content</span></div>
  <div class="row" style="top:418px"><span class="row__head">Sample Row Heading</span>
    <span class="cell c1">Content</span><span class="cell c2">Content</span><span class="cell c3">Content</span><span class="cell c4">Content</span><span class="cell c5">Content</span></div>
  <div class="row" style="top:480px"><span class="row__head">Sample Row Heading</span>
    <span class="cell c1">Content</span><span class="cell c2 cell--key">Content</span><span class="cell c3">Content</span><span class="cell c4">Content</span><span class="cell c5">Content</span></div>
  <div class="row" style="top:543px"><span class="row__head">Sample Row Heading</span>
    <span class="cell c1">Content</span><span class="cell c2">Content</span><span class="cell c3">Content</span><span class="cell c4">Content</span><span class="cell c5">Content</span></div>

  <div class="footer-line footer-line--left"></div>
  <div class="footer-dot footer-dot--navy"></div>
  <span class="deck-title">Sample Presentation Title</span>
  <span class="page-number">10</span>
  <div class="footer-dot footer-dot--green"></div>
  <div class="footer-line footer-line--right"></div>

  <ul class="notes">
    <li>Source: Sample source text</li>
    <li>¹ Sample notes text 1</li>
    <li>² Sample notes text 2</li>
  </ul>
</main>
</body>
</html>
```